Elegant & Eye-Catching Brochure- Photo Booth Rentals

We rent photo booths for weddings, sweet 16's, parties, mitzvah's, school and corporate events and we would like to create a vibrant and fun, yet professional brochure to be attractive to the entire spectrum of potential clients. The brochure will be the standard tri-fold style (8.5"x11") and will have 3 inside panels and 3 outside panels.

Ideally this brochure would be elegant, classy, and professional, but still vibrant and fun. We have many colorful images that convey the quality of our photos and options, we want to highlight that aspect, but also would like to maintain that we are a great selection for weddings. Thus we stress the classy yet fun aspect of this project. Also, it would be preferable to use legible and interesting, but clear fonts. Clean and less cluttered is also a plus, but by all means just do what you think looks best.

Attached are the photos that we have available and fit our goals. There is no need to use them all, but if possible please stress the great range of options and the lovely clean wedding shots. Blue, White, Silver and a splash of pink have been used in the past for our logo, site, business cards, and older brochures so those are the preferred colors for this brochure. This brochure should trend feminine. Most of our clients are brides and mothers so that should be taken into consideration, but only to a point so that we don't close ourselves off to anyone.

I am attaching a logo, some photos strips, single shots, and instructions on the actual wording. Please let me know if you need anything else. Thank you in advance.
Updates

Target Market(s)

most of our clients are female, but the brochure shouldn't be so feminine as to dissuade males from becoming clients

Industry/Entity Type

School

Colors
f9d9e8
ffffff
f0f0f0
86cae7

Requirements
Nice to have
• A way of fitting in a variety of colorful photos to highlight our range, but while still maintaining a clean and ordered look.

```html
<!DOCTYPE html>
<html lang="en">
<head>
<meta charset="utf-8">
<title>Harbor Light Photo Booths – Tri-fold Brochure</title>
<link href="https://fonts.googleapis.com/css2?family=Great+Vibes&family=Open+Sans:wght@400;600;700&display=swap" rel="stylesheet">
<style>
  :root{
    --page:#ffffff;
    --sky:#c6e4ea;
    --sky-deep:#86cae7;
    --pink:#f4a3c4;
    --pink-soft:#f9d9e8;
    --silver:#f0f0f0;
    --ink:#3a3a3a;
    --heading-blue:#3ea6dc;
    --frame-grey:#6d6d6d;
    --script-grey:#6f7a80;
  }
  *{box-sizing:border-box;margin:0;padding:0}
  html,body{width:1200px;height:1000px;overflow:hidden;background:var(--page)}
  body{position:relative;font-family:"Open Sans",Arial,sans-serif;color:var(--ink)}

  .brochure{position:absolute;left:127px;top:135px;width:946px;height:730px;background:var(--sky);
    box-shadow:0 6px 14px rgba(0,0,0,.25)}
  .panel{position:absolute;top:0;height:730px}
  .panel--packages{left:0;width:318px}
  .panel--inside{left:318px;width:312px;border-left:1px solid rgba(0,0,0,.06)}
  .panel--cover{left:630px;width:316px;border-left:1px solid rgba(0,0,0,.06)}

  .pink-band{position:absolute;background:var(--pink);height:12px}

  .title-banner{position:absolute;left:52px;top:12px;width:200px;height:64px}
  .title-banner__text{position:absolute;left:0;top:14px;width:200px;text-align:center;
    font-family:"Great Vibes",cursive;font-size:34px;color:#555}

  .package{position:absolute;left:17px;width:290px}
  .package__name{font-family:"Great Vibes",cursive;font-size:21px;color:var(--heading-blue);font-weight:400;line-height:1}
  .list{list-style:none;font-size:10.5px;line-height:12px}
  .list li::before{content:"• "}
  .included__title{font-size:12.5px;font-weight:700;text-decoration:underline;letter-spacing:.2px;margin-bottom:3px}

  .photo{position:absolute}
  .essentials{position:absolute;left:18px;top:212px;width:290px}
  .essentials__title{font-size:13px;font-weight:700;margin-bottom:1px}

  .strips{position:absolute;left:-2px;top:318px;width:314px;height:233px}
  .strip{position:absolute;top:0;height:233px;width:76px}

  .brand{position:absolute;display:flex;align-items:center;justify-content:center;gap:8px;
    border:2px solid var(--frame-grey);background:rgba(255,255,255,.35)}
  .brand__name{font-family:"Open Sans",Arial,sans-serif;font-weight:700;color:#555;font-size:17px}
  .brand__mark{width:14px;height:14px;background:var(--frame-grey)}

  .contact{position:absolute;left:0;top:656px;width:312px;text-align:center;font-size:12.5px;font-weight:700;line-height:15.5px;color:#444}

  .badge{position:absolute;left:6px;top:7px;width:64px;height:62px;background:var(--sky-deep);border:2px solid #fff}
  .tagline{position:absolute;left:0;top:688px;width:316px;text-align:center;font-family:"Great Vibes",cursive;font-size:23px;color:var(--script-grey)}
</style>
</head>
<body>
<main class="brochure">

  <section class="panel panel--packages">
    <div class="pink-band" style="left:0;top:62px;width:318px"></div>
    <svg class="title-banner" viewBox="0 0 200 64" aria-hidden="true">
      <path d="M6 8 H194 V54 H6 Z" fill="var(--silver)" stroke="#555" stroke-width="2"/>
      <path d="M12 13 H188 V49 H12 Z" fill="none" stroke="#777" stroke-width="1"/>
    </svg>
    <div class="title-banner__text" style="left:52px;top:22px">Packages</div>

    <div class="package" style="top:120px">
      <h2 class="package__name">The Happy Bride</h2>
      <ul class="list">
        <li>The Basic Package</li><li>Scrapbook</li>
        <li>Your Choice of Social Media Kiosk, Green Screen, or Specialty Booth Upgrade</li>
        <li>Print Per Person, per session</li>
      </ul>
    </div>
    <div class="package" style="top:212px">
      <h2 class="package__name">The Party Girl Package</h2>
      <ul class="list">
        <li>Basic Package</li><li>Scrapbook</li><li>Party Booth Upgrade</li>
        <li>Double Prints (2 strips per session becomes 4)</li>
      </ul>
    </div>
    <div class="package" style="top:293px">
      <h2 class="package__name">The Brand Builder Package</h2>
      <ul class="list">
        <li>Basic Package</li><li>Social Media Kiosk</li>
        <li>Custom Branded Step &amp; Repeat Banner</li><li>Branded Prints</li>
      </ul>
    </div>
    <div class="package" style="top:374px">
      <h2 class="package__name">The Perfect Package</h2>
      <ul class="list">
        <li>Basic Package</li><li>Scrapbook</li>
        <li>Social Media Kiosk, Gatsby or Hollywood Upgrade</li>
        <li>Print Per Person</li><li>100 2x6 Photo Frames</li>
        <li>100 Photo Frame Placecard Inserts (designed by you or us)</li>
      </ul>
    </div>
    <div class="package" style="top:489px">
      <h3 class="included__title">EACH RENTAL PACKAGE COMES WITH:</h3>
      <ul class="list">
        <li>Your Choice of Classic or Open Booth.</li>
        <li>4 Hour Photo Booth Rental.</li>
        <li>Professionally, Amazing, and Well Dressed Photo Booth Attendant.</li>
        <li>High Quality Photography &amp; Lighting for the Finest Photos.</li>
        <li>(2) 2x6 Photo Strips per session.</li>
        <li>Your Choice of Backdrop- over 10 colors to choose from.</li>
        <li>Your Choice of Accent Curtain for Classic Booth rentals.</li>
        <li>Your Choice of Caption &amp; Style to commemorate your event.</li>
        <li>Digital Copies of all images.</li>
        <li>Access to a password protected gallery and free downloads for your guests.</li>
        <li>Prop Box with all the essentials.</li>
      </ul>
    </div>
  </section>

  <section class="panel panel--inside">
    <div class="pink-band" style="left:0;top:62px;width:312px"></div>
    <div class="photo" role="img" aria-label="Glittery keepsake scrapbook with a couple's photo on the cover, resting on a wooden table"
      style="left:18px;top:81px;width:275px;height:117px;border:2px solid #fff;background:linear-gradient(90deg,#b4521f,#2f4b52 30%,#2a4850 70%,#c0602a)"></div>

    <div class="essentials">
      <h3 class="essentials__title">ESSENTIALS</h3>
      <ul class="list">
        <li>Double Prints per session</li><li>Print per Person each session</li>
        <li>Plastic Sleeves</li><li>2x6 acrylic frames &amp; 4x6 acrylic frames</li>
        <li>Placecard Inserts for your Frames</li><li>Scrapbook</li>
      </ul>
    </div>

    <div class="strips">
      <div class="strip" role="img" aria-label="Photo strip of a wedding couple embracing" style="left:0;background:linear-gradient(#5a3a30,#3a2520)"></div>
      <div class="strip" role="img" aria-label="Photo strip of a bride and groom posing" style="left:80px;background:linear-gradient(#9a9a9a,#d8d8d8)"></div>
      <div class="strip" role="img" aria-label="Photo strip of friends in party props" style="left:159px;background:linear-gradient(#6e6e6e,#b0b0b0)"></div>
      <div class="strip" role="img" aria-label="Photo strip of a couple before a turquoise backdrop" style="left:239px;background:linear-gradient(#2a9fc4,#5cc0de)"></div>
    </div>

    <div class="brand" style="left:38px;top:529px;width:227px;height:110px">
      <span class="brand__mark"></span><span class="brand__name">Harbor Light Photo Booths</span>
    </div>

    <address class="contact" style="font-style:normal">
      p: 555.014.2273<br>
      e: hello@harborlightbooths.com<br>
      www.harborlightbooths.com<br>
      Brookfield Falls, NJ
    </address>
  </section>

  <section class="panel panel--cover">
    <div class="photo" role="img" aria-label="Group of friends posing with photo booth props"
      style="left:0;top:8px;width:316px;height:219px;background:linear-gradient(135deg,#7c7480,#a89590 50%,#5f5660)"></div>
    <div class="badge" role="img" aria-label="Wedding listing award badge"></div>

    <div class="brand" style="left:18px;top:230px;width:282px;height:105px">
      <span class="brand__mark"></span><span class="brand__name">Harbor Light Photo Booths</span>
    </div>

    <div class="photo" role="img" aria-label="Bride and groom sharing a kiss in the photo booth"
      style="left:0;top:337px;width:316px;height:298px;background:radial-gradient(circle at 50% 55%,#8a6a55,#a88a6e 50%,#7a6048)"></div>
    <div class="pink-band" style="left:0;top:635px;width:316px"></div>
    <p class="tagline">Make Memories on Your Special Day</p>
  </section>

</main>
</body>
</html>
```